HVAC company business card design

We need a business card design for a HVAC company. The design must look professional. Both sides will be used. The total data to be on the business card is
Name
Position
Email
Direct Phone/Moile Phone
Company Contacts /Address, Phone, Fax, web)
All data will be submit once the design is confirmed. For generic purposes use;
Emre Toksoy
Managing Director
+902324815263 (Mobile)
4712 Sokak No: 9 KBSE Yenikent IZMIR TURKEY
Tel: +902324815263 Fax : +902324815269
www.luvon.com.tr

Target Market(s)

HVAC

Industry/Entity Type

Business

Contact Information for Business Card

The total data to be on the business card is
Name
Position
Email
Direct Phone/Moile Phone
Emre Toksoy
Managing Director
+902324815263 (Mobile)
www.luvon.com.tr
The BC will use both sides of the card. The front will include the full logo and the details for the business card holder. The business card can be divided into vertical/horizontal or to a special shape. The common data like the company address/phone/fax should be indicated elsewehere. The back can contain some part or the whole logo and must contain the web address.

Font styles to use
Serif
Sans Serif

Colors
0355a3
cfdfed

Requirements
Should not have
• Please be careful with the fonts, it shouldnt be too small or too big and must not interfere with the logo fonts. If you need to use a curvy shape please do not use as the logo is already curvy or use the curves from the logo (if it looks good, otherwise forget it)
• We are not in favor of pictograms, only if they are perfect use them.

```html
<!DOCTYPE html>
<html lang="en">
<head>
<meta charset="utf-8">
<title>Luvon business card</title>
<link href="https://fonts.googleapis.com/css2?family=Arimo:wght@400;700&display=swap" rel="stylesheet">
<style>
  :root{
    --page:#e8eaee;
    --navy:#3b4a6e;
    --navy-deep:#34426a;
    --navy-shade:#2f3c60;
    --blue:#3a7bc6;
    --blue-light:#4a8ad2;
    --paper:#f5f6f7;
    --ink:#3a4766;
    --text-light:#ffffff;
    --text-soft:#d4e0ee;
  }
  *{margin:0;padding:0;box-sizing:border-box}
  html,body{width:1200px;height:1023px;overflow:hidden;background:var(--page);font-family:"Arimo",Arial,sans-serif}
  .sheet{position:relative;width:1200px;height:1023px}
  .card{position:absolute;left:250px;width:700px;height:400px;overflow:hidden;box-shadow:0 6px 18px rgba(30,40,70,.25)}
  .card--front{top:70px;background:var(--paper)}
  .card--back{top:553px;background:var(--navy)}
  .card__art{position:absolute;inset:0}
  .contact{position:absolute;color:var(--text-light);font-size:15px;line-height:26px;display:flex;gap:10px;align-items:flex-start}
  .contact__lines{text-align:right}
  .contact__icons{display:flex;flex-direction:column;gap:4px;margin-top:2px}
  .contact--phones{right:438px;top:48px}
  .contact--office{right:438px;top:290px}
  .icon{width:22px;height:22px;background:var(--blue);display:block}
  .holder{position:absolute;left:0;top:158px;width:300px;text-align:center;color:var(--text-light)}
  .holder__name{font-size:24px;font-weight:700;letter-spacing:.2px}
  .holder__role{font-size:15px;color:var(--text-soft);margin-top:6px}
  .brand{position:absolute;left:400px;top:168px;display:flex;align-items:center;gap:14px}
  .brand__dot{width:48px;height:48px;border-radius:50%;background:var(--blue)}
  .brand__name{font-size:52px;font-weight:700;color:var(--ink);letter-spacing:2px}
  .web{position:absolute;left:40px;top:188px;color:var(--text-light);font-size:16px;letter-spacing:.3px}
</style>
</head>
<body>
<main class="sheet">

  <section class="card card--front" aria-label="Front of card">
    <svg class="card__art" viewBox="0 0 700 400" aria-hidden="true">
      <rect x="0" y="0" width="290" height="400" fill="var(--navy)"/>
      <polygon points="0,0 290,0 290,150 0,150" fill="var(--navy-deep)"/>
      <polygon points="0,140 290,140 370,110 290,150 0,150" fill="var(--navy-shade)" opacity=".6"/>
      <polygon points="0,150 290,150 370,118 370,282 290,250 0,250" fill="var(--blue)"/>
      <polygon points="290,150 370,118 370,150 290,170" fill="var(--blue-light)"/>
      <rect x="688" y="165" width="12" height="70" fill="var(--blue)"/>
    </svg>

    <div class="contact contact--phones">
      <div class="contact__lines"><div>+902324815263</div><div>+902324815263</div></div>
      <div class="contact__icons">
        <svg class="icon" viewBox="0 0 22 22" aria-label="Phone"><rect width="22" height="22" fill="var(--blue)"/><rect x="7" y="4" width="8" height="14" rx="1.5" fill="none" stroke="#fff" stroke-width="1.6"/></svg>
        <svg class="icon" viewBox="0 0 22 22" aria-label="Fax"><rect width="22" height="22" fill="var(--blue)"/><rect x="5" y="8" width="12" height="8" fill="none" stroke="#fff" stroke-width="1.6"/><rect x="7" y="4" width="8" height="4" fill="#fff"/></svg>
      </div>
    </div>

    <div class="holder">
      <div class="holder__name">Emre Toksoy</div>
      <div class="holder__role">Managing Director</div>
    </div>

    <div class="contact contact--office">
      <div class="contact__lines"><div>+902324815269</div><div>info@luvon.com.tr</div></div>
      <div class="contact__icons">
        <svg class="icon" viewBox="0 0 22 22" aria-label="Phone"><rect width="22" height="22" fill="var(--blue)"/><rect x="7" y="4" width="8" height="14" rx="1.5" fill="none" stroke="#fff" stroke-width="1.6"/></svg>
        <svg class="icon" viewBox="0 0 22 22" aria-label="Email"><rect width="22" height="22" fill="var(--blue)"/><rect x="4" y="6" width="14" height="10" fill="none" stroke="#fff" stroke-width="1.6"/><polyline points="4,6 11,12 18,6" fill="none" stroke="#fff" stroke-width="1.6"/></svg>
      </div>
    </div>

    <div class="brand">
      <span class="brand__dot"></span>
      <span class="brand__name">LUVON</span>
    </div>
  </section>

  <section class="card card--back" aria-label="Back of card">
    <svg class="card__art" viewBox="0 0 700 400" aria-hidden="true">
      <polygon points="0,0 220,0 220,150 0,150" fill="var(--navy-deep)"/>
      <line x1="220" y1="0" x2="220" y2="400" stroke="var(--navy-shade)" stroke-width="2"/>
      <line x1="0" y1="250" x2="700" y2="300" stroke="var(--navy-shade)" stroke-width="1.5" opacity=".7"/>
      <polygon points="0,150 220,150 280,140 300,168 280,180 320,250 0,250" fill="var(--blue)"/>
      <circle cx="290" cy="160" r="8" fill="none" stroke="#fff" stroke-width="1.5"/>
      <line x1="282" y1="160" x2="298" y2="160" stroke="#fff" stroke-width="1.2"/>
      <ellipse cx="290" cy="160" rx="3.5" ry="8" fill="none" stroke="#fff" stroke-width="1.2"/>
    </svg>
    <div class="web">www.luvon.com.tr</div>
  </section>

</main>
</body>
</html>
```